A layout of a webpage for oil trade platform

I would like to have a desgin of one page webpage (with section scrollling dowin) that woulf present the new product i.e. oil trade platform for wholesale buyers and sellers.
Layout should consist of the sections similar to the given at: https://strona.trawomirek.pl/modul-planowania-spotkan
However oil industy require more colors and more photo stories than here for doctor.
I. I woul imagine at first below menu a slider with brueg information about the product and its advantages with "more" button next to the prict screen of our platform on different displays (PC and mobile).
II. Bellow the slider I would imagine icons correspoing to the advantages of that plaftorm:
1. Purchase/sale process automation 24/7
2. Access to the best deals
3. Electronic offerings and orderings
4. Transaction status monitoring
5. Data and transaction security
II A) (optional):
In near future we would like to prepare a short video presenation. Hence please prepare a place to display that element here.
At the moment alternatvily please prepare a How it works section that would explan the platform operating process
III. Next secion is about benefits for Oil Purchaser
It can be done either by icons of by text and corresponding grahip for while section.
Benefits:
- Access to cheaper oil
- Convenience of online orders
- Possibility to compare prices on the market
- Transaction history
- Order status monitoring
- Seccurity and transparency of purchase
IV. Next seciont is about benefits for Oil Seller
Benefits:
- New sale channel
- Attracting new clients
- More oil sold
- Transaction security
- Possibility to integrate with distribution infrastructure and logistits for more efficient automation.
V. Contact form
VI. Footer
I would need a layout that that will correspond to the very dynamic logo but I would expect also a clean form, smoth and modern. It has to be proffessional layout with more corporate character.
It can use a paralax features if needed.
Attachments:
- logo design
- platfrom print screen
Industry/Entity Type
Oil And Gas
Number of Pages Required
1 page

```html
<!DOCTYPE html>
<html lang="en">
<head>
<meta charset="utf-8">
<title>Oilvanta – Online Oil Trading</title>
<link rel="stylesheet" href="https://fonts.googleapis.com/css2?family=Roboto:wght@300;400;500;700&family=Roboto+Condensed:wght@400;700&display=swap">
<style>
:root{
  --navy:#17274a;
  --navy-deep:#101d3a;
  --orange:#e4552b;
  --orange-soft:#ea6a3c;
  --ink:#3a3d42;
  --grey:#8d9097;
  --line:#b9bcc2;
  --paper:#ffffff;
  --form:#e8ebf0;
  --ok:#5cb85c;
  --link:#3b7dd8;
}
*{box-sizing:border-box;margin:0;padding:0}
html,body{width:1200px;height:3103px;overflow:hidden}
body{position:relative;font-family:"Roboto",Arial,sans-serif;color:var(--ink);background:var(--paper)}
.abs{position:absolute}

/* hero */
.hero{position:absolute;left:0;top:0;width:1200px;height:517px;background:linear-gradient(135deg,#1d2f55 0%,var(--navy) 55%,var(--navy-deep) 100%);overflow:hidden}
.brand{position:absolute;left:161px;top:30px;display:flex;align-items:center;gap:10px;color:#fff;font-family:"Roboto Condensed",Arial,sans-serif;font-weight:700;font-size:28px;letter-spacing:1px}
.brand-dot{width:34px;height:34px;border-radius:50%;background:var(--orange)}
.nav{position:absolute;left:509px;top:42px;display:flex;gap:22px;font-size:11px;color:#fff;text-transform:uppercase;letter-spacing:.2px}
.hero-kicker{position:absolute;left:161px;top:142px;font-size:24px;font-weight:300;color:#fff}
.hero-title{position:absolute;left:159px;top:178px;font-family:"Roboto Condensed",Arial,sans-serif;font-weight:700;font-size:50px;color:var(--orange);letter-spacing:-.5px}
.hero-text{position:absolute;left:161px;top:252px;width:410px;font-size:11.5px;line-height:17px;color:#c9d0de}
.btn-more{position:absolute;left:161px;top:347px;width:120px;height:34px;border:1.5px solid #fff;color:#fff;font-size:11px;font-weight:500;display:flex;align-items:center;justify-content:center;gap:6px;text-transform:uppercase}

/* device screens: platform dashboard */
.screen{position:absolute;background:#fff;overflow:hidden}
.dash{position:absolute;left:0;top:0;width:472px;height:287px;display:flex;font-size:7px;color:#555;background:#fff;transform-origin:0 0}
.dash-side{width:62px;background:#3c4049;color:#cfd3da;padding-top:10px;text-align:center}
.dash-avatar{display:block;width:30px;height:30px;margin:0 auto 4px;border-radius:50%;background:#c9cdd4}
.dash-user{font-size:6.5px;margin-bottom:10px}
.dash-side ul{list-style:none;text-align:left}
.dash-side li{padding:5px 6px;border-top:1px solid #4b505a;font-size:6.5px}
.dash-side li.on{background:#2c2f36}
.dash-main{flex:1;padding:0}
.dash-title{height:20px;line-height:20px;padding-left:8px;font-size:9px;color:#333;background:#f2f3f5;border-bottom:1px solid #dde0e4}
.dash-tools{display:flex;justify-content:space-between;padding:6px 8px}
.dash-input{width:50px;height:10px;border:1px solid #d7dade}
.dash-input.wide{width:70px}
.dash-table{width:calc(100% - 16px);margin:0 8px;border-collapse:collapse}
.dash-table th{text-align:left;font-weight:700;font-size:6.5px;padding:4px 3px;background:#f4f5f7;border-bottom:1px solid #dde0e4}
.dash-table td{padding:6px 3px;border-bottom:1px solid #eceef1;font-size:6.5px;color:#666}
.dash-table td.link{color:var(--link)}
.chip{display:inline-block;padding:1px 4px;background:var(--ok);color:#fff;border-radius:2px;font-size:6px}
.dash-foot{margin:6px 8px;font-size:6px;color:#999}
.mini{position:absolute;left:0;top:0;width:100%;height:100%;font-size:5px;color:#555}
.mini-title{height:12px;line-height:12px;padding-left:4px;background:#f2f3f5;border-bottom:1px solid #dde0e4;font-size:6px}
.mini-row{display:flex;gap:3px;padding:4px 4px;border-bottom:1px solid #eceef1;align-items:center}
.mini-row span{height:3px;background:#cfd3d9;flex:1}
.mini-row i{width:7px;height:4px;background:var(--ok)}

/* features */
.features{position:absolute;left:0;top:517px;width:1200px;height:157px;background:#fff}
.feature{position:absolute;top:30px;width:190px;margin-left:-95px;text-align:center;font-size:13px;line-height:16px;color:var(--grey)}
.feature svg{display:block;margin:0 auto 8px}

/* how it works */
.how-photo{position:absolute;left:0;top:674px;width:559px;height:487px;background:linear-gradient(160deg,#7a6a5a 0%,#c47a45 45%,#4b3a2e 100%)}
.how{position:absolute;left:559px;top:674px;width:641px;height:487px;background:linear-gradient(120deg,var(--orange) 0%,var(--orange-soft) 100%);color:#fff}
.how h2{position:absolute;left:68px;top:42px;font-family:"Roboto Condensed",Arial,sans-serif;font-weight:700;font-size:34px}
.how .sub{position:absolute;left:68px;top:84px;font-size:12px;text-transform:uppercase}
.how .intro{position:absolute;left:68px;top:110px;width:410px;font-size:11px;line-height:16px;color:#ffe3d6}
.how .lead{position:absolute;left:68px;top:182px;font-size:16px;font-weight:500}
.step{position:absolute;left:68px;width:520px;height:60px}
.step-num{position:absolute;left:0;top:0;width:52px;height:52px;border-radius:50%;background:#fff;border:3px solid #f7c7b3;color:var(--ink);font-weight:700;font-size:22px;display:flex;align-items:center;justify-content:center}
.step-title{position:absolute;left:66px;top:2px;font-size:13px;font-weight:700;color:#fff}
.step-text{position:absolute;left:66px;top:20px;width:340px;font-size:10.5px;line-height:14px;color:#ffe3d6}

/* section titles */
.sec-title{position:absolute;left:0;width:1200px;text-align:center}
.sec-title h2{font-family:"Roboto Condensed",Arial,sans-serif;font-weight:700;font-size:42px;color:var(--ink);line-height:44px}
.sec-title p{font-size:25px;font-weight:300;color:var(--grey);text-transform:uppercase;letter-spacing:.5px}

/* purchaser benefits */
.benefit{position:absolute;width:420px;height:90px}
.benefit-icon{position:absolute;left:0;top:0;width:74px;height:74px;border:2px solid var(--line);display:flex;align-items:center;justify-content:center}
.benefit h3{position:absolute;left:100px;top:0;font-size:16px;font-weight:400;color:var(--ink)}
.benefit p{position:absolute;left:100px;top:24px;width:310px;font-size:11px;line-height:16px;color:var(--grey)}

/* video */
.video{position:absolute;left:0;top:1682px;width:1200px;height:335px;background:linear-gradient(180deg,#5a5f70 0%,#8a7a78 45%,#c08a5a 70%,#2a2a30 100%)}
.play{position:absolute;left:567px;top:133px;width:66px;height:66px;border-radius:50%;background:rgba(255,255,255,.85);display:flex;align-items:center;justify-content:center}

/* seller cards */
.card{position:absolute;width:279px;height:199px;background:var(--orange);border:2px solid var(--orange)}
.card-photo{width:100%;height:170px}
.card-label{height:25px;display:flex;align-items:center;justify-content:center;color:#fff;font-size:13px;font-weight:500;text-transform:uppercase}

/* contact */
.contact{position:absolute;left:0;top:2665px;width:1200px;height:381px;background:linear-gradient(135deg,#1d2f55,var(--navy-deep))}
.contact-card{position:absolute;left:225px;top:31px;width:748px;height:317px;background:var(--form)}
.contact-card h2{position:absolute;left:0;top:70px;width:100%;text-align:center;font-family:"Roboto Condensed",Arial,sans-serif;font-weight:700;font-size:28px;color:var(--navy)}
.contact-card .sub{position:absolute;left:0;top:106px;width:100%;text-align:center;font-family:"Roboto Condensed",Arial,sans-serif;font-size:13px;color:var(--navy);text-transform:uppercase}
.envelope{position:absolute;left:352px;top:18px;width:44px;height:44px;border-radius:50%;border:2px solid var(--navy);display:flex;align-items:center;justify-content:center}
.field{position:absolute;height:33px;background:#e1e5eb;border:1px solid #d2d7de;display:flex;align-items:center;gap:10px;padding-left:12px;font-size:11px;color:#9aa0a8}
.btn-send{position:absolute;left:278px;top:259px;width:190px;height:33px;background:var(--navy);color:#fff;font-family:"Roboto Condensed",Arial,sans-serif;font-weight:700;font-size:15px;display:flex;align-items:center;justify-content:center;gap:8px;text-transform:uppercase}

/* footer */
.footer{position:absolute;left:0;top:3046px;width:1200px;height:57px;background:var(--orange);color:#fff}
.footer-links{position:absolute;left:161px;top:15px;font-size:10.5px}
.footer-copy{position:absolute;left:161px;top:34px;font-size:9.5px;color:#ffe0d2}
.social{position:absolute;top:18px;width:22px;height:22px;border-radius:50%;background:#fff;opacity:.85}
</style>
</head>
<body>

<header class="hero">
  <div class="brand"><span class="brand-dot"></span>OILVANTA</div>
  <nav class="nav"><span>Home</span><span>How it works</span><span>Benefits for oil purchaser</span><span>Benefits for oil seller</span><span>Contact us</span></nav>
  <p class="hero-kicker">wholesale buyers and sellers</p>
  <h1 class="hero-title">ONLINE OIL TRADING</h1>
  <p class="hero-text">Lorem Ipsum is simply dummy text of the printing and typesetting industry. Lorem Ipsum has been the industry's standard dummy text ever since the 1500s, when an unknown printer took Lorem Ipsum is simply dummy text of the printing ...</p>
  <div class="btn-more">Read more
    <svg width="12" height="12" viewBox="0 0 12 12"><circle cx="6" cy="6" r="6" fill="#fff"/><path d="M5 3.5 7.5 6 5 8.5" stroke="#17274a" stroke-width="1.6" fill="none"/></svg>
  </div>

  <!-- desktop monitor -->
  <div class="abs" style="left:617px;top:141px;width:500px;height:315px;background:#0d0d10;border-radius:6px"></div>
  <div class="screen" style="left:631px;top:155px;width:472px;height:287px">
    <div class="dash">
      <div class="dash-side"><span class="dash-avatar"></span><p class="dash-user">buyer</p>
        <ul><li class="on">Dashboard</li><li>Orders</li><li>Offers</li><li>Settings</li></ul></div>
      <div class="dash-main">
        <p class="dash-title">My orders</p>
        <div class="dash-tools"><span class="dash-input"></span><span class="dash-input wide"></span></div>
        <table class="dash-table">
          <tr><th>Date</th><th>Supplier</th><th>Product</th><th>Amount</th><th>Price</th><th>Status</th></tr>
          <tr><td>12.03.17</td><td>Nordline</td><td>Diesel</td><td class="link">25 000 l</td><td>3.42</td><td><span class="chip">paid</span></td></tr>
          <tr><td>14.03.17</td><td>Vestoil</td><td>Heating</td><td class="link">18 000 l</td><td>2.95</td><td><span class="chip">paid</span></td></tr>
          <tr><td>20.03.17</td><td>Baltpetro</td><td>Diesel</td><td class="link">30 000 l</td><td>3.38</td><td><span class="chip">paid</span></td></tr>
          <tr><td>27.03.17</td><td>Nordline</td><td>Petrol</td><td class="link">12 000 l</td><td>3.61</td><td><span class="chip">paid</span></td></tr>
          <tr><td>02.04.17</td><td>Vestoil</td><td>Diesel</td><td class="link">22 000 l</td><td>3.40</td><td><span class="chip">paid</span></td></tr>
        </table>
        <p class="dash-foot">Showing 1 to 5</p>
      </div>
    </div>
  </div>
  <div class="abs" style="left:840px;top:456px;width:60px;height:30px;background:#2a2c33"></div>
  <div class="abs" style="left:800px;top:486px;width:140px;height:8px;background:#2a2c33;border-radius:3px"></div>

  <!-- laptop -->
  <div class="abs" style="left:484px;top:348px;width:277px;height:160px;background:#0d0d10;border-radius:6px 6px 0 0"></div>
  <div class="screen" style="left:494px;top:358px;width:257px;height:146px">
    <div class="dash" style="transform:scale(.545)">
      <div class="dash-side"><span class="dash-avatar"></span><p class="dash-user">buyer</p>
        <ul><li class="on">Dashboard</li><li>Orders</li><li>Offers</li><li>Settings</li></ul></div>
      <div class="dash-main">
        <p class="dash-title">My orders</p>
        <div class="dash-tools"><span class="dash-input"></span><span class="dash-input wide"></span></div>
        <table class="dash-table">
          <tr><th>Date</th><th>Supplier</th><th>Product</th><th>Amount</th><th>Price</th><th>Status</th></tr>
          <tr><td>12.03.17</td><td>Nordline</td><td>Diesel</td><td class="link">25 000 l</td><td>3.42</td><td><span class="chip">paid</span></td></tr>
          <tr><td>14.03.17</td><td>Vestoil</td><td>Heating</td><td class="link">18 000 l</td><td>2.95</td><td><span class="chip">paid</span></td></tr>
          <tr><td>20.03.17</td><td>Baltpetro</td><td>Diesel</td><td class="link">30 000 l</td><td>3.38</td><td><span class="chip">paid</span></td></tr>
          <tr><td>27.03.17</td><td>Nordline</td><td>Petrol</td><td class="link">12 000 l</td><td>3.61</td><td><span class="chip">paid</span></td></tr>
          <tr><td>02.04.17</td><td>Vestoil</td><td>Diesel</td><td class="link">22 000 l</td><td>3.40</td><td><span class="chip">paid</span></td></tr>
        </table>
        <p class="dash-foot">Showing 1 to 5</p>
      </div>
    </div>
  </div>
  <div class="abs" style="left:460px;top:506px;width:325px;height:11px;background:#c6c9cf;border-radius:0 0 6px 6px"></div>

  <!-- tablet -->
  <div class="abs" style="left:1051px;top:331px;width:118px;height:176px;background:#0d0d10;border-radius:10px"></div>
  <div class="screen" style="left:1059px;top:345px;width:102px;height:148px">
    <div class="mini">
      <p class="mini-title">My orders</p>
      <div class="mini-row" style="font-weight:700"><b style="flex:1">Date</b><b style="flex:1">Product</b><b style="flex:1">Status</b></div>
      <div class="mini-row"><span></span><span></span><i></i></div>
      <div class="mini-row"><span></span><span></span><i></i></div>
      <div class="mini-row"><span></span><span></span><i></i></div>
      <div class="mini-row"><span></span><span></span><i></i></div>
      <div class="mini-row"><span></span><span></span><i></i></div>
      <div class="mini-row"><span></span><span></span><i></i></div>
      <div class="mini-row"><span></span><span></span><i></i></div>
    </div>
  </div>

  <!-- phone -->
  <div class="abs" style="left:1028px;top:424px;width:58px;height:93px;background:#f4f5f7;border:2px solid #c8cbd1;border-radius:8px"></div>
  <div class="screen" style="left:1033px;top:436px;width:48px;height:68px;border:1px solid #dde0e4">
    <div class="mini">
      <div class="mini-title" style="height:8px"></div>
      <div class="mini-row" style="padding:3px"><span></span><i></i></div>
      <div class="mini-row" style="padding:3px"><span></span><i></i></div>
      <div class="mini-row" style="padding:3px"><span></span><i></i></div>
      <div class="mini-row" style="padding:3px"><span></span><i></i></div>
      <div class="mini-row" style="padding:3px"><span></span><i></i></div>
      <div class="mini-row" style="padding:3px"><span></span><i></i></div>
    </div>
  </div>
</header>

<section class="features">
  <div class="feature" style="left:230px">
    <svg width="60" height="60" viewBox="0 0 60 60" fill="none" stroke="#9a9da3" stroke-width="3"><path d="M52 30a22 22 0 1 1-8-17"/><path d="M46 6v9h-9"/><text x="30" y="36" text-anchor="middle" font-family="Roboto,Arial,sans-serif" font-size="17" font-weight="700" fill="#9a9da3" stroke="none">24</text></svg>
    Purchase/sale process<br>automation 24/7
  </div>
  <div class="feature" style="left:424px">
    <svg width="60" height="60" viewBox="0 0 60 60"><circle cx="30" cy="30" r="26" fill="none" stroke="#9a9da3" stroke-width="4" stroke-dasharray="5 3"/><circle cx="30" cy="30" r="19" fill="#9a9da3"/><path d="M21 30l6 6 12-12" stroke="#fff" stroke-width="4" fill="none"/></svg>
    Access to the best<br>deals
  </div>
  <div class="feature" style="left:604px">
    <svg width="60" height="60" viewBox="0 0 60 60" fill="none" stroke="#9a9da3" stroke-width="2.5"><rect x="15" y="15" width="30" height="30"/><rect x="22" y="22" width="16" height="16" fill="#9a9da3"/><path d="M21 15V6M30 15V6M39 15V6M21 45v9M30 45v9M39 45v9M15 21H6M15 30H6M15 39H6M45 21h9M45 30h9M45 39h9"/></svg>
    Electronic offerings<br>and orderings
  </div>
  <div class="feature" style="left:795px">
    <svg width="60" height="60" viewBox="0 0 60 60" fill="none" stroke="#9a9da3" stroke-width="3"><rect x="6" y="8" width="48" height="34" rx="2"/><path d="M24 42v8M36 42v8M18 51h24"/><circle cx="30" cy="25" r="9"/><path d="M30 19v6h5"/></svg>
    Transaction status<br>monitoring
  </div>
  <div class="feature" style="left:977px">
    <svg width="60" height="60" viewBox="0 0 60 60" fill="none" stroke="#9a9da3" stroke-width="3"><rect x="4" y="18" width="40" height="28" rx="2"/><path d="M4 26h40"/><text x="16" y="42" font-family="Roboto,Arial,sans-serif" font-size="13" font-weight="700" fill="#9a9da3" stroke="none">$</text><path d="M40 8l14 5v10c0 9-6 14-14 17-8-3-14-8-14-17V13z" fill="#fff"/><path d="M34 22l5 5 8-9"/></svg>
    Data and transaction<br>security
  </div>
</section>

<div class="how-photo" role="img" aria-label="Photo of an oil worker in a hard hat holding a clipboard at a refinery"></div>
<section class="how">
  <h2>HOW IT WORKS</h2>
  <p class="sub">Oil trade platform</p>
  <p class="intro">Lorem Ipsum is simply dummy text of the printing and typesetting industry. Lorem Ipsum has been the industry's standard dummy text ever since the 1500s, when an unknown printer took a galley of type and scrambled it to make a type specimen book centuries.</p>
  <p class="lead">Lorem Ipsum is simply dummy text of the printing...</p>
  <div class="step" style="top:229px"><div class="step-num">01</div><p class="step-title">Lorem Ipsum is simply dummy text of the printing...</p><p class="step-text">industry. Lorem Ipsum has been the industry's standard dummy text ever centuries, but also the leap into electronic typesetting, remaining.</p></div>
  <div class="step" style="top:310px"><div class="step-num">02</div><p class="step-title">Lorem Ipsum is simply dummy text of the printing...</p><p class="step-text">industry. Lorem Ipsum has been the industry's standard dummy text ever centuries, but also the leap into electronic typesetting, remaining.</p></div>
  <div class="step" style="top:388px"><div class="step-num">03</div><p class="step-title">Lorem Ipsum is simply dummy text of the printing...</p><p class="step-text">industry. Lorem Ipsum has been the industry's standard dummy text ever centuries, but also the leap into electronic typesetting, remaining.</p></div>
</section>

<div class="sec-title" style="top:1205px"><h2>BENEFITS</h2><p>For oil purchaser</p></div>

<div class="benefit" style="left:161px;top:1334px">
  <div class="benefit-icon"><svg width="40" height="40" viewBox="0 0 40 40" fill="#8d9097"><path d="M8 10h18l2 4H10z"/><path d="M10 16h16v18H10z"/><path d="M32 18c3 4 4 6 4 8a4 4 0 0 1-8 0c0-2 1-4 4-8z"/></svg></div>
  <h3>Access to cheaper oil</h3><p>Lorem Ipsum is simply dummy text of the printing and typesetting industry. Lorem Ipsum has been the industry's standard dummy text</p>
</div>
<div class="benefit" style="left:161px;top:1443px">
  <div class="benefit-icon"><svg width="44" height="40" viewBox="0 0 44 40" fill="none" stroke="#8d9097" stroke-width="2.5"><rect x="3" y="9" width="24" height="18"/><path d="M27 15h8l5 6v6H27"/><circle cx="11" cy="30" r="3.5" fill="#fff"/><circle cx="33" cy="30" r="3.5" fill="#fff"/></svg></div>
  <h3>Convenience of online orders</h3><p>Lorem Ipsum is simply dummy text of the printing and typesetting industry. Lorem Ipsum has been the industry's standard dummy text</p>
</div>
<div class="benefit" style="left:161px;top:1557px">
  <div class="benefit-icon"><svg width="44" height="44" viewBox="0 0 44 44" fill="none" stroke="#8d9097" stroke-width="2.5"><circle cx="22" cy="22" r="18" stroke-dasharray="4 2"/><circle cx="22" cy="22" r="12"/><text x="22" y="28" text-anchor="middle" font-family="Roboto,Arial,sans-serif" font-size="16" font-weight="700" fill="#8d9097" stroke="none">$</text></svg></div>
  <h3>Possibility to compare prices on the market</h3><p>Lorem Ipsum is simply dummy text of the printing and typesetting industry. Lorem Ipsum has been the industry's standard dummy text</p>
</div>
<div class="benefit" style="left:648px;top:1334px">
  <div class="benefit-icon"><svg width="44" height="40" viewBox="0 0 44 40" fill="none" stroke="#8d9097" stroke-width="2.5"><path d="M4 8h16l2 2 2-2h16v26H24l-2 2-2-2H4z"/><path d="M22 10v24M9 15h8M9 20h8M9 25h8M27 15h8M27 20h8M27 25h8"/></svg></div>
  <h3>Transaction history</h3><p>Lorem Ipsum is simply dummy text of the printing and typesetting industry. Lorem Ipsum has been the industry's standard dummy text</p>
</div>
<div class="benefit" style="left:648px;top:1443px">
  <div class="benefit-icon"><svg width="44" height="40" viewBox="0 0 44 40" fill="none" stroke="#8d9097" stroke-width="2.5"><rect x="4" y="4" width="36" height="24" rx="1"/><path d="M18 28v6M26 28v6M13 35h18"/><circle cx="22" cy="16" r="6"/><path d="M22 12v4h3"/></svg></div>
  <h3>Order status monitoring</h3><p>Lorem Ipsum is simply dummy text of the printing and typesetting industry. Lorem Ipsum has been the industry's standard dummy text</p>
</div>
<div class="benefit" style="left:648px;top:1557px">
  <div class="benefit-icon"><svg width="40" height="44" viewBox="0 0 40 44"><path d="M12 20v-7a8 8 0 0 1 16 0v7" fill="none" stroke="#8d9097" stroke-width="3"/><rect x="7" y="20" width="26" height="20" rx="2" fill="#8d9097"/><circle cx="20" cy="29" r="3" fill="#fff"/><path d="M20 30v5" stroke="#fff" stroke-width="2"/></svg></div>
  <h3>Seccurity and transparency of purchase</h3><p>Lorem Ipsum is simply dummy text of the printing and typesetting industry. Lorem Ipsum has been the industry's standard dummy text</p>
</div>

<section class="video" role="img" aria-label="Refinery towers and pipework at dusk, video presentation placeholder">
  <div class="play"><svg width="26" height="28" viewBox="0 0 26 28"><path d="M4 2l20 12L4 26z" fill="#3a3d42"/></svg></div>
</section>

<div class="sec-title" style="top:2064px"><h2>BENEFITS</h2><p>For oil seller</p></div>

<div class="card" style="left:161px;top:2175px"><div class="card-photo" role="img" aria-label="Photo of oil pipelines" style="background:linear-gradient(135deg,#cfd3d8,#7e858e)"></div><div class="card-label">New sale channel</div></div>
<div class="card" style="left:459px;top:2175px"><div class="card-photo" role="img" aria-label="Photo of two workers shaking hands at an industrial site" style="background:linear-gradient(135deg,#b8c2cc,#6f7a60)"></div><div class="card-label">Attracting new clients</div></div>
<div class="card" style="left:757px;top:2175px"><div class="card-photo" role="img" aria-label="Photo of oil pouring from a can" style="background:linear-gradient(135deg,#aab0b8,#c88a2a)"></div><div class="card-label">More oil sold</div></div>
<div class="card" style="left:314px;top:2404px"><div class="card-photo" role="img" aria-label="Photo of a hand holding a phone with a security alert" style="background:linear-gradient(135deg,#caa896,#b2332a)"></div><div class="card-label">Transaction security</div></div>
<div class="card" style="left:612px;top:2404px"><div class="card-photo" role="img" aria-label="Photo of orange automated industrial machinery" style="background:linear-gradient(135deg,#e3a13a,#8b8f96)"></div><div class="card-label">Efficient automation</div></div>

<section class="contact">
  <div class="contact-card">
    <div class="envelope"><svg width="22" height="16" viewBox="0 0 22 16" fill="none" stroke="#17274a" stroke-width="2"><rect x="1" y="1" width="20" height="14"/><path d="M1 1l10 8 10-8"/></svg></div>
    <h2>GET IN TOUCH WITH US:</h2>
    <p class="sub">Fill your data and send us!</p>
    <div class="field" style="left:19px;top:147px;width:321px"><svg width="11" height="11" viewBox="0 0 11 11" fill="#9aa0a8"><circle cx="5.5" cy="3" r="3"/><path d="M0 11a5.5 5 0 0 1 11 0z"/></svg>Name</div>
    <div class="field" style="left:350px;top:147px;width:377px"><svg width="11" height="11" viewBox="0 0 11 11" fill="#9aa0a8"><circle cx="5.5" cy="3" r="3"/><path d="M0 11a5.5 5 0 0 1 11 0z"/></svg>Address</div>
    <div class="field" style="left:19px;top:201px;width:321px"><svg width="12" height="9" viewBox="0 0 12 9" fill="#9aa0a8"><path d="M0 0h12v9H0z"/><path d="M0 0l6 5 6-5" stroke="#e1e5eb" fill="none"/></svg>Email ID</div>
    <div class="field" style="left:350px;top:201px;width:377px"><svg width="11" height="11" viewBox="0 0 11 11" fill="#9aa0a8"><path d="M2 0l2 3-1 1.5a7 7 0 0 0 3.5 3.5L8 7l3 2-1.5 2C4 11 0 7 0 1.5z"/></svg>Phone Number</div>
    <div class="btn-send"><svg width="14" height="14" viewBox="0 0 14 14"><rect x="0" y="0" width="14" height="14" rx="3" fill="#fff"/><path d="M4 7h6M7 4l3 3-3 3" stroke="#17274a" stroke-width="1.6" fill="none"/></svg>Send quote!</div>
  </div>
</section>

<footer class="footer">
  <p class="footer-links">Home &nbsp;|&nbsp; How it works &nbsp;|&nbsp; Benefits for Oil Purchaser &nbsp;|&nbsp; Benefits for Oil Seller &nbsp;|&nbsp; Contact Us</p>
  <p class="footer-copy">Copyright © 2017 oilvanta | Privacy policy</p>
  <span class="social" style="left:920px"></span>
  <span class="social" style="left:951px"></span>
  <span class="social" style="left:984px"></span>
  <span class="social" style="left:1015px"></span>
</footer>

</body>
</html>
```